ICT Company specialising in web based information system design and implementation

We need a design for a new company in Australia called "Harbor QDT". We design and develop customised web based information systems to automate business processes. This design needs to be based around Bootstrap from Gravelo (http://gravelo.codeshelf-demo.com/)

Industry/Entity Type

Business

Requirements
Must have
• based on bootstrap gravelo, site will be hosted on conrete5 platform. (http://gravelo.codeshelf-demo.com/)

```html
<!DOCTYPE html>
<html lang="en">
<head>
<meta charset="utf-8">
<title>Harbor QDT</title>
<link rel="stylesheet" href="https://fonts.googleapis.com/css2?family=Arimo:wght@400;700&family=Roboto:wght@300;400&display=swap">
<style>
  :root {
    --bg: #eef1f1;
    --rule: #d6dcdc;
    --brand-blue: #1b6d9e;
    --muted: #6b6f70;
    --footer-text: #9a9d9e;
    --green: #2a9b20;
    --sky: #1b8ac4;
    --navy: #1d4d78;
    --red: #c8161a;
    --ribbon: #1fa0d8;
    --ribbon-dark: #137fb6;
    --panel-bg: #e6f0f1;
    --panel-border: #a7dbe8;
    --body-text: #3a3d3e;
    --social: #9aa6ab;
    --nav-rule: #b9c0c2;
  }
  * { margin: 0; padding: 0; box-sizing: border-box; }
  html, body { width: 1200px; height: 606px; overflow: hidden; }
  body {
    background: var(--bg);
    font-family: "Arimo", Arial, sans-serif;
    position: relative;
  }
  .site-header { position: absolute; left: 0; top: 0; width: 1200px; height: 85px; border-bottom: 1px solid var(--rule); }
  .brand { position: absolute; left: 59px; top: 24px; display: flex; align-items: center; gap: 22px; white-space: nowrap; }
  .brand-mark { width: 46px; height: 46px; border-radius: 50%; background: var(--brand-blue); }
  .brand-name { font-size: 23px; font-weight: 700; color: var(--brand-blue); letter-spacing: 0.5px; }
  .follow { position: absolute; right: 40px; top: 48px; display: flex; align-items: center; gap: 6px; white-space: nowrap; }
  .follow-label { font-size: 17px; color: var(--muted); margin-right: 6px; }
  .social-dot { width: 26px; height: 26px; border-radius: 4px; background: var(--social); }

  .main-nav { position: absolute; left: 0; top: 0; }
  .nav-item { position: absolute; display: flex; align-items: center; white-space: nowrap; }
  .nav-item .label { font-size: 19px; font-weight: 700; letter-spacing: 0.3px; line-height: 1; white-space: nowrap; }
  .nav-rule { position: absolute; height: 1px; background: var(--nav-rule); }
  .nav-about .label { color: var(--green); }
  .nav-projects .label { color: var(--sky); }
  .nav-skills .label { color: var(--navy); }
  .nav-contact .label { color: var(--red); }

  .globe-shadow { position: absolute; left: 420px; top: 488px; width: 270px; height: 26px; border-radius: 50%; background: radial-gradient(ellipse, rgba(0,0,0,0.22), rgba(0,0,0,0) 70%); }
  .globe {
    position: absolute; left: 358px; top: 116px; width: 394px; height: 394px; border-radius: 50%;
    background: radial-gradient(circle at 62% 30%, #bfe8fb 0%, #55bff0 30%, #1d8fd8 65%, #0c5fa8 100%);
  }

  .about-panel {
    position: absolute; left: 830px; top: 151px; width: 330px; height: 369px;
    background: var(--panel-bg); border: 1px solid var(--panel-border);
    padding-top: 18px;
  }
  .about-panel p { font-size: 14.5px; line-height: 26px; color: var(--body-text); text-align: center; white-space: nowrap; }
  .ribbon { position: absolute; left: 803px; top: 102px; }
  .ribbon-title { position: absolute; left: 847px; top: 110px; width: 281px; text-align: center; font-size: 24px; font-weight: 700; color: #fff; white-space: nowrap; }

  .site-footer { position: absolute; left: 0; top: 547px; width: 1200px; height: 59px; border-top: 1px solid var(--rule); }
  .site-footer p { font-family: "Roboto", Arial, sans-serif; font-weight: 300; font-size: 14.5px; color: var(--footer-text); text-align: center; margin-top: 18px; word-spacing: 1px; white-space: nowrap; }
</style>
</head>
<body>
  <header class="site-header">
    <div class="brand">
      <span class="brand-mark"></span>
      <span class="brand-name">HARBOR QDT</span>
    </div>
    <div class="follow">
      <span class="follow-label">Follow me on</span>
      <span class="social-dot"></span>
      <span class="social-dot"></span>
      <span class="social-dot"></span>
      <span class="social-dot"></span>
      <span class="social-dot"></span>
    </div>
  </header>

  <nav class="main-nav">
    <div class="nav-rule" style="left:224px;top:168px;width:180px"></div>
    <div class="nav-item nav-about" style="left:195px;top:137px">
      <svg width="38" height="38" viewBox="0 0 38 38" aria-hidden="true">
        <defs><radialGradient id="infoFill" cx="40%" cy="30%" r="70%"><stop offset="0" stop-color="#6fa6ee"/><stop offset="1" stop-color="#1744a8"/></radialGradient></defs>
        <circle cx="19" cy="19" r="18" fill="url(#infoFill)"/>
        <circle cx="19" cy="10.5" r="3" fill="#fff"/>
        <rect x="16.5" y="15.5" width="5" height="14" rx="1" fill="#fff"/>
      </svg>
      <span class="label" style="margin-left:10px">ABOUT US</span>
    </div>

    <div class="nav-rule" style="left:118px;top:279px;width:272px"></div>
    <div class="nav-item nav-projects" style="left:65px;top:242px">
      <div role="img" aria-label="Project sheet icon" style="width:56px;height:50px;background:linear-gradient(160deg,#ffffff,#dfe4e6);border-radius:4px;transform:rotate(-18deg)"></div>
      <span class="label" style="margin-left:18px">OUR PROJECTS</span>
    </div>

    <div class="nav-rule" style="left:53px;top:385px;width:325px"></div>
    <div class="nav-item nav-skills" style="left:53px;top:348px">
      <svg width="42" height="42" viewBox="0 0 42 42" aria-hidden="true">
        <rect x="2" y="26" width="10" height="14" rx="1" fill="#e8641c"/>
        <rect x="15" y="14" width="10" height="26" rx="1" fill="#1f7fcf"/>
        <rect x="28" y="2" width="10" height="38" rx="1" fill="#5bb22c"/>
      </svg>
      <span class="label" style="margin-left:12px">SKILL AND EXPERIENCE</span>
    </div>

    <div class="nav-rule" style="left:165px;top:494px;width:248px"></div>
    <div class="nav-item nav-contact" style="left:165px;top:462px">
      <svg width="44" height="34" viewBox="0 0 44 34" aria-hidden="true">
        <path d="M4 12 Q22 0 40 12 L38 17 L31 15 L30 11 Q22 8 14 11 L13 15 L6 17 Z" fill="#3b6fb0"/>
        <path d="M10 16 L34 16 L40 32 L4 32 Z" fill="#4a84c6"/>
        <circle cx="22" cy="24" r="5.5" fill="#d9e6f3"/>
        <circle cx="22" cy="24" r="2" fill="#3b6fb0"/>
      </svg>
      <span class="label" style="margin-left:12px">CONTACT US</span>
    </div>
  </nav>

  <div class="globe-shadow"></div>
  <div class="globe" role="img" aria-label="Glossy blue globe with continents and grid lines"></div>

  <svg class="ribbon" width="369" height="56" viewBox="0 0 369 56" aria-hidden="true">
    <polygon points="0,12 56,12 56,48 0,48 14,30" fill="var(--ribbon-dark)"/>
    <polygon points="369,12 313,12 313,48 369,48 355,30" fill="var(--ribbon-dark)"/>
    <polygon points="44,40 56,48 56,40" fill="#0d5f8a"/>
    <polygon points="325,40 313,48 313,40" fill="#0d5f8a"/>
    <path d="M44 4 Q184 -2 325 4 L325 40 Q184 34 44 40 Z" fill="var(--ribbon)"/>
  </svg>
  <div class="ribbon-title">ABOUT US</div>

  <section class="about-panel">
    <p>Lorem ipsum dolor sit ipsum&nbsp; Lorem ipsum<br>
    dolor sit ipsum Lorem ipsum dolor sit<br>
    ipsum Lorem ipsum dolor sit ipsum Lorem<br>
    ipsum dolor sit ipsum Lorem ipsum dolor<br>
    sit ipsum Lorem ipsum dolor sit ipsum<br>
    Lorem ipsum dolor sit ipsum&nbsp; Lorem ipsum<br>
    dolor sit ipsum Lorem ipsum dolor sit<br>
    ipsum Lorem ipsum dolor sit ipsum Lorem<br>
    ipsum dolor sit ipsum Lorem ipsum dolor<br>
    sit ipsumolor sit ipsum Lorem ipsum dolor<br>
    sit ipsum Lorem ipsum dolor sit ipsumolor<br>
    sit ipsum Lorem ipsum dolor sit ipsum<br>
    Lorem ipsum dolor sit ipsum</p>
  </section>

  <footer class="site-footer">
    <p>Copyright @ 2012&nbsp; Harbor QDT&nbsp;&nbsp;&nbsp;&nbsp; Design and Developed by : XYZ Company name</p>
  </footer>
</body>
</html>
```